Business / Stationery Design Project

Hi,

I need business cards and all other stationary designed for my new finance broking business.

Stationary required:

Business card
Letter head
with compliments
envelopes

There is gold in the logo design so some gold would be good and open to other creative ideas / colours.

Regards
Milo
Updates

Target Market(s)

Small to medium business customers. Also to appeal to referrers who include accounting firms and other associated professionals (valuers etc)

Industry/Entity Type

Finance

Requirements
Must have
• Professional, classy look.

```html
<!DOCTYPE html>
<html lang="en">
<head>
<meta charset="utf-8">
<title>Hartley Finance — Business Card</title>
<link rel="stylesheet" href="https://fonts.googleapis.com/css2?family=Titillium+Web:wght@400;600&display=swap">
<style>
  :root {
    --stage: #d9d9d9;
    --stage-edge: #bdbdbd;
    --paper: #fbfbfa;
    --ink: #1e1e1e;
    --band: #262626;
    --text-grey: #3a3a3a;
    --muted-grey: #8a8a8a;
    --gold: #c9a24a;
    --card-black: #1b1b1b;
    --light: #f4f4f4;
  }
  * { box-sizing: border-box; margin: 0; padding: 0; }
  html, body { width: 1200px; height: 900px; overflow: hidden; }
  body {
    background: radial-gradient(ellipse at 50% 40%, var(--stage) 0%, var(--stage-edge) 100%);
    font-family: "Titillium Web", Arial, sans-serif;
    position: relative;
  }
  .card {
    position: absolute;
    left: 280px;
    width: 640px;
    height: 366px;
    border-radius: 3px;
    box-shadow: 0 10px 28px rgba(0,0,0,0.22);
    overflow: hidden;
  }
  .card--front { top: 50px; background: var(--paper); }
  .card--back { top: 474px; background: var(--card-black); }

  .name-band {
    position: absolute;
    left: 0; top: 64px;
    width: 370px; height: 44px;
    background: var(--band);
    display: flex; align-items: center;
    padding-left: 44px;
    color: #f2f2f2;
  }
  .name-band__name { font-size: 22px; font-weight: 600; letter-spacing: 0.3px; }
  .name-band__role { font-size: 15px; font-weight: 400; margin-left: 8px; color: #d8d8d8; }

  .edge-block {
    position: absolute;
    right: 0; top: 136px;
    width: 44px; height: 62px;
    background: var(--band);
  }

  .brand {
    position: absolute;
    display: flex;
    align-items: center;
    gap: 10px;
    font-weight: 600;
    line-height: 1;
    white-space: nowrap;
  }
  .brand__dot {
    width: 12px; height: 12px;
    border-radius: 50%;
    background: var(--gold);
    flex: none;
  }
  .card--front .brand { left: 368px; top: 152px; font-size: 28px; color: var(--ink); }
  .card--back .brand { left: 0; top: 164px; width: 640px; justify-content: center; font-size: 38px; color: var(--light); }

  .contact {
    position: absolute;
    left: 44px; top: 226px;
    color: var(--text-grey);
    font-size: 15px;
    line-height: 21px;
  }
  .contact__address { font-size: 17px; margin-bottom: 4px; }
  .contact__label { color: var(--gold); font-weight: 600; display: inline-block; width: 16px; }
  .contact__highlight { color: var(--gold); }

  .web-line {
    position: absolute;
    left: 36px; bottom: 26px;
    font-size: 15px;
    color: var(--muted-grey);
  }
  .web-line__highlight { color: var(--gold); }
</style>
</head>
<body>
  <section class="card card--front" aria-label="Business card front">
    <div class="name-band">
      <span class="name-band__name">Milo Hartley</span>
      <span class="name-band__role">| Director</span>
    </div>
    <div class="brand">
      <span class="brand__dot"></span>
      <span class="brand__name">Hartley Finance</span>
    </div>
    <div class="edge-block"></div>
    <div class="contact">
      <p class="contact__address">112 Carrick Ave, ROSEBANK SA 5072</p>
      <p><span class="contact__label">M</span>0400 128 476</p>
      <p><span class="contact__label">E</span>milo@hartleyfinance.com.au</p>
      <p><span class="contact__label">W</span>www.<span class="contact__highlight">hartleyfinance</span>.com.au</p>
    </div>
  </section>

  <section class="card card--back" aria-label="Business card back">
    <div class="brand">
      <span class="brand__dot"></span>
      <span class="brand__name">Hartley Finance</span>
    </div>
    <p class="web-line">www.<span class="web-line__highlight">hartleyfinance</span>.com.au</p>
  </section>
</body>
</html>
```